Design a Web Development Agency Website

This project is to design a website for a Web Development Agency named Mavorix.
Please design the landing page first and if your design is selected then you can design the Services, About Us, and Portfolio page.
This web agency is targeted to the African market specifically small businesses in Nigeria so the design should be modern, professional, clean and elegant.

The name of the company as shall appear in the footer is Mavorix Communications Ltd.

Industry/Entity Type

Web design, small to med sized business

Number of Pages Required

4 page

Font styles to use
Sans Serif

Colors
00AB8E
00BBA5
67D7C9
C6EFE9
E9F9F6
F0912C
F2A743
F7CA91
FBE8D2
FDF5EE

Requirements
Must have
• Professional, clean home page, MUST deliver in Figma

```html
<!DOCTYPE html>
<html lang="en">
<head>
<meta charset="utf-8">
<title>Mavorix – Web Development Agency</title>
<link href="https://fonts.googleapis.com/css2?family=Poppins:wght@400;500;600;700&display=swap" rel="stylesheet">
<style>
:root{
  --teal:#00AB8E;
  --teal-2:#00BBA5;
  --teal-3:#67D7C9;
  --teal-4:#C6EFE9;
  --teal-5:#E9F9F6;
  --orange:#F0912C;
  --orange-2:#F2A743;
  --orange-3:#F7CA91;
  --orange-4:#FBE8D2;
  --orange-5:#FDF5EE;
  --blue:#1E6FE8;
  --navy:#1B2646;
  --ink:#2B2F3A;
  --muted:#6B7280;
  --line:#E3E7EC;
  --footer:#1E1E24;
  --white:#fff;
}
*{box-sizing:border-box;margin:0;padding:0}
html,body{width:1200px;height:4012px;overflow:hidden}
body{position:relative;font-family:'Poppins',sans-serif;color:var(--ink);background:var(--white)}
.abs{position:absolute}
p{font-size:15px;line-height:1.65;color:var(--muted)}
.btn{display:inline-block;border-radius:24px;font-weight:600;font-size:14px;color:#fff;background:var(--orange-2);padding:11px 26px}

/* Header & hero */
.hero{left:0;top:0;width:1200px;height:560px;background:linear-gradient(180deg,var(--teal-2),var(--teal));border-bottom-left-radius:50% 60px;border-bottom-right-radius:50% 60px;overflow:hidden}
.hero-ring{left:-120px;top:360px;width:380px;height:380px;border-radius:50%;border:40px solid rgba(255,255,255,.08)}
.brand{left:110px;top:22px;color:#fff}
.brand .name{font-size:30px;font-weight:700;line-height:1}
.brand .tag{font-size:11px;font-weight:500;letter-spacing:.5px;margin-top:4px}
.nav{left:486px;top:30px;display:flex;gap:30px;font-size:15px;color:#fff}
.nav .active{color:var(--orange-3);border-bottom:2px solid var(--orange-2);padding-bottom:3px}
.quote{left:944px;top:20px}
.hero-title{left:110px;top:236px;font-size:62px;font-weight:700;color:#fff;line-height:1}
.hero-text{left:110px;top:318px;width:360px;color:#fff;font-size:14px}
.hero-btn{left:110px;top:386px}
.hero-photo{left:640px;top:40px;width:480px;height:500px;border-radius:240px 240px 0 0;background:radial-gradient(circle at 50% 40%,var(--teal-3),var(--teal) 70%)}
.hero-dots{left:540px;top:120px;width:120px;height:120px;border-radius:50%;background:var(--teal-3);opacity:.35}

/* Feature cards */
.features{left:120px;top:550px;width:960px;display:flex;gap:30px}
.feature{flex:1;background:#fff;border-radius:6px;box-shadow:0 10px 30px rgba(20,40,60,.12);padding:28px 28px 30px;height:250px}
.feature svg{width:62px;height:62px;margin-bottom:12px}
.feature h3{font-size:21px;font-weight:600;color:var(--ink);margin-bottom:10px}
.feature p{font-size:14px}

/* About */
.about-blob{left:130px;top:850px;width:300px;height:300px;border-radius:50%;background:var(--orange-2)}
.about-art{left:110px;top:900px;width:470px;height:380px;border-radius:16px;background:linear-gradient(135deg,#3a3f4b,#8f96a4 60%,#c9ccd4)}
.about-title{left:600px;top:868px;font-size:48px;font-weight:700;color:var(--navy)}
.about-title span{color:var(--blue)}
.about-rule{left:600px;top:942px;width:70px;height:3px;background:var(--navy)}
.about-text{left:600px;top:962px;width:490px}
.about-text p{font-size:13.5px;line-height:1.6}
.about-btn{left:600px;top:1290px}

/* Stats */
.stats{left:0;top:1390px;width:1200px;height:290px;background:var(--teal-5)}
.stat{top:1480px;width:200px}
.stat .num{font-size:40px;font-weight:600;line-height:1.1}
.stat p{font-size:13px;line-height:1.5;margin-top:6px}
.stat-div{top:1470px;width:1px;height:100px;background:var(--line)}
.ring-orange{left:1090px;top:1610px;width:170px;height:170px;border-radius:50%;border:18px solid var(--orange-2)}

/* Portfolio */
.section-title{left:0;width:1200px;text-align:center;font-weight:700;color:var(--navy)}
.section-title span{color:var(--blue)}
.portfolio-title{top:1752px;font-size:48px}
.pf-side{top:1890px;width:340px;height:250px;border-radius:6px}
.pf-left{left:10px;background:linear-gradient(135deg,#dfe8dd,#b9cbb5)}
.pf-right{left:850px;background:linear-gradient(135deg,#e4ecfb,#9ab8f0)}
.pf-arrow{top:1985px;width:56px;height:56px;border-radius:50%;background:#1b2a4a}
.pf-main{left:370px;top:1860px;width:460px;height:320px;border-radius:10px;background:#f3f4f6;border:10px solid #e5e7eb;box-shadow:0 24px 40px rgba(0,0,0,.15)}
.pf-main .screen{position:absolute;inset:0;background:linear-gradient(160deg,#1e3a8a,#2563eb 60%,#dbe7fb)}
.pf-name{top:2198px;font-size:20px;font-weight:600;color:var(--ink)}
.pf-text{left:400px;top:2234px;width:400px;text-align:center;font-size:14px}
.pf-btn{left:526px;top:2292px;background:var(--blue)}
.ring-left{left:-90px;top:2360px;width:170px;height:170px;border-radius:50%;border:18px solid var(--orange-2)}

/* Testimonials */
.reviews{left:0;top:2420px;width:1200px;height:560px;background:var(--teal-5)}
.reviews-title{top:2494px;font-size:42px}
.reviews-title span{color:var(--orange-2)}
.rv-dot-l{left:92px;top:2780px;width:70px;height:70px;border-radius:50%;background:var(--blue)}
.rv-dot-r{left:1080px;top:2680px;width:36px;height:72px;border-radius:36px 0 0 36px;background:var(--teal-3)}
.review{top:2592px;width:300px;height:360px;background:#fff;border-radius:4px;padding:26px 28px;box-shadow:0 8px 24px rgba(0,0,0,.06)}
.review.t1{border-top:4px solid var(--teal-2)}
.review.t2{border-top:4px solid var(--teal)}
.review.t3{border-top:4px solid var(--orange-2)}
.review .q{font-size:40px;font-weight:700;line-height:.8;color:var(--teal)}
.review p{font-size:13.5px;margin-top:8px}
.review .who{position:absolute;left:28px;bottom:26px;display:flex;align-items:center;gap:12px;border-top:1px solid var(--line);padding-top:16px;width:244px}
.avatar{width:44px;height:44px;border-radius:50%;background:var(--teal-4)}
.who b{display:block;font-size:14px;font-weight:600;color:var(--ink)}
.who small{font-size:12px;color:var(--muted)}

/* Contact */
.contact-title{top:3112px;font-size:48px}
.field{height:52px;border:1px solid var(--line);border-radius:3px;background:#fff;padding:14px 18px;font-size:13px;color:#9aa1ab}
.f-area{height:120px}
.remember{left:362px;top:3472px;font-size:13px;color:var(--muted);display:flex;align-items:center;gap:8px}
.remember i{width:14px;height:14px;border:1px solid #aaa;border-radius:50%;display:block}
.submit{left:520px;top:3462px;width:170px;text-align:center;letter-spacing:3px}
.captcha{left:720px;top:3462px;width:200px;height:46px;border:1px solid var(--line);border-radius:3px;background:#f9f9f9}

/* Newsletter & footer */
.footer{left:0;top:3700px;width:1200px;height:312px;background:var(--footer)}
.newsletter{left:110px;top:3624px;width:980px;height:160px;background:var(--teal);border-radius:4px}
.nl-title{left:170px;top:3650px;color:#fff;font-size:44px;line-height:1.2}
.nl-title b{display:block;font-weight:600}
.nl-input{left:540px;top:3676px;width:500px;height:52px;border-radius:26px;background:#fff;padding:15px 24px;font-size:13px;color:#9aa1ab}
.nl-btn{left:858px;top:3682px;padding:10px 24px}
.foot-brand{left:110px;top:3820px}
.foot-nav{left:380px;top:3840px;display:flex;gap:18px;font-size:14px;color:#fff}
.foot-nav span.sep{color:#777}
.socials{left:940px;top:3830px;display:flex;gap:10px}
.socials i{display:block;width:30px;height:30px;border-radius:50%;border:1.5px solid #fff}
.foot-rule{left:110px;top:3912px;width:980px;height:1px;background:#3a3a42}
.copy{left:0;top:3938px;width:1200px;text-align:center;color:#fff;font-size:13px}
</style>
</head>
<body>

<section class="abs hero" aria-label="Hero">
  <div class="abs hero-ring"></div>
</section>
<div class="abs hero-dots"></div>
<div class="abs hero-photo" role="img" aria-label="Photo of a smiling man in a green shirt holding an open laptop"></div>
<header>
  <div class="abs brand"><div class="name">Mavorix</div><div class="tag">COMMUNICATIONS LTD</div></div>
  <nav class="abs nav"><span class="active">Home</span><span>About us</span><span>Services</span><span>Reviews</span><span>Contact us</span></nav>
  <span class="abs btn quote">Get a Quote</span>
</header>
<h1 class="abs hero-title">Mavorix</h1>
<p class="abs hero-text">Lorem ipsum dolor sit amet, consectetur adipiscing elit, sed do eiusmod tempor incididunt ut labore.</p>
<span class="abs btn hero-btn">Get Started</span>

<section class="abs features">
  <article class="feature">
    <svg viewBox="0 0 62 62" fill="none" stroke="#1E6FE8" stroke-width="2"><rect x="8" y="10" width="46" height="32" rx="3"/><path d="M24 52h14M31 42v10"/><path d="M16 32l8-8 6 6 10-10" stroke="#F0912C"/></svg>
    <h3>Duis aute irure dolor</h3>
    <p>Lorem ipsum dolor sit amet, consectetur adipiscing elit, sed do eiusmod tempor incididunt ut labore</p>
  </article>
  <article class="feature">
    <svg viewBox="0 0 62 62" fill="none" stroke="#00AB8E" stroke-width="2"><path d="M8 52h48M8 52V10"/><path d="M12 44l12-14 10 8 18-22"/><path d="M44 16h8v8" stroke="#F0912C"/></svg>
    <h3>Duis aute irure dolor</h3>
    <p>Lorem ipsum dolor sit amet, consectetur adipiscing elit, sed do eiusmod tempor incididunt ut labore</p>
  </article>
  <article class="feature">
    <svg viewBox="0 0 62 62" fill="none" stroke="#F0912C" stroke-width="2"><path d="M8 54h48"/><rect x="12" y="34" width="8" height="20"/><rect x="27" y="24" width="8" height="30"/><rect x="42" y="12" width="8" height="42"/></svg>
    <h3>Duis aute irure dolor</h3>
    <p>Lorem ipsum dolor sit amet, consectetur adipiscing elit, sed do eiusmod tempor incididunt ut labore</p>
  </article>
</section>

<div class="abs about-blob"></div>
<div class="abs about-art" role="img" aria-label="Illustration of a laptop showing a programming website"></div>
<h2 class="abs about-title">About <span>Mavorix</span></h2>
<div class="abs about-rule"></div>
<div class="abs about-text">
  <p>Lorem ipsum dolor sit amet, consectetur adipiscing elit, sed do eiusmod tempor incididunt ut labore et dolore magna aliqua. Ut enim ad minim veniam, quis nostrud exercitation ullamco laboris nisi ut aliquip ex ea commodo consequat. Duis aute irure dolor in reprehenderit in voluptate velit esse cillum dolore eu fugiat nulla pariatur.</p>
  <p style="margin-top:14px">Excepteur sint occaecat cupidatat non proident, sunt in culpa qui officia deserunt mollit anim id est laborum. Lorem ipsum dolor sit amet, consectetur adipiscing elit, sed do eiusmod tempor incididunt ut labore et dolore magna aliqua. Ut enim ad minim veniam, quis nostrud exercitation ullamco laboris nisi ut aliquip ex ea commodo consequat.</p>
</div>
<span class="abs btn about-btn">Learn more</span>

<section class="abs stats" aria-label="Key figures"></section>
<div class="abs stat" style="left:110px"><div class="num" style="color:var(--blue)">3M+</div><p>3M+ Customers across the world</p></div>
<div class="abs stat-div" style="left:370px"></div>
<div class="abs stat" style="left:410px"><div class="num" style="color:var(--teal)">5year</div><p>5years industry Experience</p></div>
<div class="abs stat-div" style="left:640px"></div>
<div class="abs stat" style="left:676px"><div class="num" style="color:var(--orange-2)">4.5</div><p>4.5 star rating based on 250 reviews</p></div>
<div class="abs stat-div" style="left:930px"></div>
<div class="abs stat" style="left:1000px"><div class="num" style="color:var(--navy)">25k+</div><p>25k+ Business accounts</p></div>
<div class="abs ring-orange"></div>

<h2 class="abs section-title portfolio-title">Our <span>Portfolio</span></h2>
<div class="abs pf-side pf-left" role="img" aria-label="Screenshot of a plant shop website"></div>
<div class="abs pf-side pf-right" role="img" aria-label="Screenshot of a programming website"></div>
<div class="abs pf-arrow" style="left:124px"><svg viewBox="0 0 56 56" width="56" height="56"><path d="M34 18l-10 10 10 10" stroke="#fff" stroke-width="3" fill="none"/></svg></div>
<div class="abs pf-arrow" style="left:1020px"><svg viewBox="0 0 56 56" width="56" height="56"><path d="M22 18l10 10-10 10" stroke="#fff" stroke-width="3" fill="none"/></svg></div>
<div class="abs pf-main"><div class="screen" role="img" aria-label="Screenshot of the agency landing page"></div></div>
<h3 class="abs section-title pf-name">Nemo enim ipsam</h3>
<p class="abs pf-text">Lorem ipsum dolor sit amet, consectetur adipiscing elit, sed do eiusmod tempor incididunt ut labore et dolore</p>
<span class="abs btn pf-btn">Learn more</span>
<div class="abs ring-left"></div>

<section class="abs reviews" aria-label="Testimonials"></section>
<h2 class="abs section-title reviews-title">What Peaple Says <span>About Us</span></h2>
<div class="abs rv-dot-l"></div>
<div class="abs rv-dot-r"></div>
<article class="abs review t1" style="left:130px">
  <div class="q">“</div>
  <p>Lorem ipsum dolor sit amet, consectetur adipiscing elit, sed do eiusmod tempor incididunt ut labore et dolore magna aliqua. Ut enim ad minim veniam, quis nostrud exercitation ullamco laboris nisi ut aliquip ex ea commodo consequat.</p>
  <div class="who"><div class="avatar" role="img" aria-label="Customer portrait"></div><div><b>John doe</b><small>Company name</small></div></div>
</article>
<article class="abs review t2" style="left:450px">
  <div class="q">“</div>
  <p>Lorem ipsum dolor sit amet, consectetur adipiscing elit, sed do eiusmod tempor incididunt ut labore et dolore magna aliqua. Ut enim ad minim veniam, quis nostrud exercitation ullamco laboris nisi ut aliquip ex ea commodo consequat.</p>
  <div class="who"><div class="avatar" role="img" aria-label="Customer portrait"></div><div><b>John doe</b><small>Company name</small></div></div>
</article>
<article class="abs review t3" style="left:770px">
  <div class="q" style="color:var(--orange-2)">“</div>
  <p>Lorem ipsum dolor sit amet, consectetur adipiscing elit, sed do eiusmod tempor incididunt ut labore et dolore magna aliqua. Ut enim ad minim veniam, quis nostrud exercitation ullamco laboris nisi ut aliquip ex ea commodo consequat.</p>
  <div class="who"><div class="avatar" role="img" aria-label="Customer portrait"></div><div><b>John doe</b><small>Company name</small></div></div>
</article>

<h2 class="abs section-title contact-title">Contact <span>Us</span></h2>
<form>
  <div class="abs field" style="left:260px;top:3204px;width:330px">First name*</div>
  <div class="abs field" style="left:610px;top:3204px;width:330px">Last name*</div>
  <div class="abs field" style="left:260px;top:3272px;width:330px">Phone*</div>
  <div class="abs field" style="left:610px;top:3272px;width:330px">Email Address*</div>
  <div class="abs field f-area" style="left:260px;top:3340px;width:680px">Note*</div>
  <div class="abs remember"><i></i>Forgot password</div>
  <span class="abs btn submit">SUBMIT</span>
  <div class="abs captcha"></div>
</form>

<footer>
  <div class="abs footer"></div>
  <div class="abs newsletter"></div>
  <h2 class="abs nl-title">Subscribe <b>Our Newsletter</b></h2>
  <div class="abs nl-input">Email address</div>
  <span class="abs btn nl-btn">Subscribe Now</span>
  <div class="abs brand foot-brand"><div class="name">Mavorix</div><div class="tag">COMMUNICATIONS LTD</div></div>
  <nav class="abs foot-nav"><span>Home</span><span class="sep">|</span><span>About us</span><span class="sep">|</span><span>Services</span><span class="sep">|</span><span>Reviews</span><span class="sep">|</span><span>Contact us</span></nav>
  <div class="abs socials" aria-label="Social links"><i></i><i></i><i></i><i></i></div>
  <div class="abs foot-rule"></div>
  <div class="abs copy">© Copyright 2022 Mavorix Communications Ltd. | All Rights Reserved</div>
</footer>

</body>
</html>
```